NZ First of it's kind solutions directory and marketplace for busy Mums needs a business card design

We need a business card design for our new nationwide business in NZ (long term plans to go global). We provide solutions to the everyday challenges that busy Mums face by connecting them with quality communities and suppliers of carefully selected, relevant products and services. We sell direct via our online marketplace. The final design should communicate our values of inclusivity, quality and smart solutions. Colours should incorporate our logo colour palette of #477077 and #6ba8b2. Our website is at https://www.brightnestly.com

Target Market(s)

busy Mums, Age 28 – 50, female, income over $100K, location main centres NZ primarily but NZ wide. Is likely juggling work or career with a young family. Probably had hobbies which have fallen by the wayside.
-Wants to succeed in her chosen career without compromising on family life
-to successfully juggle her career without feeling like she is compromising her children
- Is time poor, something always has to give and it’s generally her health (she’ll stay up late, get stressed)
- probably ex corporate or professional career. Has discretional income

Industry/Entity Type

Business

Contact Information for Business Card

Jodie Farnsworth, Founder, BrightNestly.com (Strapline Browse; Pick; Sorted), 48 Kowhai Terrace, Hillsborough, Auckland 1058, New Zealand. Mob: 021 437 518 Ph: +64 (0)9 584 7163

Font styles to use
Other font styles liked:
• Raleway, and/or Architects Daughter

Colors
00a990
33b8a4
86cfc6
cfeae6

Requirements
Must have
• the above details, streamline. the logo and colours associated with those logos
Should not have
• foil or metallic colours

```html
<!DOCTYPE html>
<html lang="en">
<head>
<meta charset="utf-8">
<title>BrightNestly business card</title>
<link href="https://fonts.googleapis.com/css2?family=Raleway:wght@700&family=Roboto+Condensed:ital,wght@0,400;0,700;1,400&display=swap" rel="stylesheet">
<style>
  :root {
    --brand-dark: #477077;
    --brand-deep: #3b5a62;
    --brand-light: #6ba8b2;
    --ink: #3a3f42;
    --card: #f7f7f7;
    --backdrop: #e3e3e3;
  }
  html, body {
    margin: 0;
    padding: 0;
    width: 1200px;
    height: 576px;
    overflow: hidden;
    background: var(--backdrop);
  }
  .canvas {
    position: relative;
    width: 1200px;
    height: 576px;
  }
  .card {
    position: absolute;
    top: 138px;
    width: 485px;
    height: 294px;
    border-radius: 16px;
    background: var(--card);
    overflow: hidden;
    font-family: "Roboto Condensed", sans-serif;
    color: var(--ink);
  }
  .card--front { left: 82px; }
  .card--back { left: 602px; width: 480px; }

  .brand {
    position: absolute;
    text-align: center;
  }
  .brand__dot {
    display: block;
    margin: 0 auto;
    border-radius: 50%;
    background: var(--brand-dark);
  }
  .brand__name {
    display: block;
    font-family: "Roboto Condensed", sans-serif;
    font-weight: 700;
    color: var(--brand-dark);
    line-height: 1;
  }
  .brand__tagline {
    display: block;
    color: var(--ink);
    text-transform: uppercase;
    line-height: 1;
  }
  .brand__tagline .sep { color: var(--brand-light); }

  .card--front .brand { left: 0; right: 0; top: 72px; }
  .card--front .brand__dot { width: 60px; height: 60px; margin-bottom: 30px; }
  .card--front .brand__name { font-size: 40px; }
  .card--front .brand__tagline { font-size: 11px; letter-spacing: 4px; margin-top: 12px; }

  .card--back .brand { left: 30px; width: 206px; top: 72px; }
  .card--back .brand__dot { width: 48px; height: 48px; margin-bottom: 30px; }
  .card--back .brand__name { font-size: 32px; }
  .card--back .brand__tagline { font-size: 9px; letter-spacing: 3px; margin-top: 10px; }

  .contact {
    position: absolute;
    left: 268px;
    top: 52px;
  }
  .contact__name {
    margin: 0;
    font-family: "Raleway", sans-serif;
    font-weight: 700;
    font-size: 20px;
    color: var(--brand-deep);
  }
  .contact__role {
    margin: 2px 0 0;
    font-style: italic;
    font-size: 12.5px;
  }
  .contact__address {
    margin: 18px 0 0;
    font-style: normal;
    font-size: 12.5px;
    line-height: 18px;
  }
  .contact__list {
    list-style: none;
    margin: 10px 0 0;
    padding: 0;
    font-size: 12.5px;
    line-height: 18px;
  }
  .contact__list li { display: flex; align-items: center; }
  .contact__list svg { width: 11px; height: 11px; margin-right: 8px; fill: var(--brand-dark); }

  .footer-band {
    position: absolute;
    left: 0;
    bottom: 0;
    width: 480px;
    height: 40px;
  }
  .website {
    position: absolute;
    left: 268px;
    bottom: 12px;
    font-size: 12.5px;
    color: #ffffff;
  }
</style>
</head>
<body>
<main class="canvas">
  <section class="card card--front" aria-label="Card front">
    <div class="brand">
      <span class="brand__dot"></span>
      <span class="brand__name">BrightNestly</span>
      <span class="brand__tagline">Browse <span class="sep">|</span> Pick <span class="sep">|</span> Sorted</span>
    </div>
  </section>

  <section class="card card--back" aria-label="Card back">
    <div class="brand">
      <span class="brand__dot"></span>
      <span class="brand__name">BrightNestly</span>
      <span class="brand__tagline">Browse <span class="sep">|</span> Pick <span class="sep">|</span> Sorted</span>
    </div>

    <div class="contact">
      <h1 class="contact__name">Jodie Farnsworth</h1>
      <p class="contact__role">Founder</p>
      <address class="contact__address">48 Kowhai Terrace, Hillsborough,<br>Auckland 1058, New Zealand</address>
      <ul class="contact__list">
        <li><svg viewBox="0 0 12 12" aria-hidden="true"><rect x="3" y="0.5" width="6" height="11" rx="1.2"/><rect x="4" y="2" width="4" height="6.5" fill="#f7f7f7"/></svg>021 437 518</li>
        <li><svg viewBox="0 0 12 12" aria-hidden="true"><path d="M1 4c0-2 2-3 5-3s5 1 5 3v1H8.5V3.5h-5V5H1z"/><path d="M2.5 6h7l1 5h-9z"/></svg>+64 (0)9 584 7163</li>
        <li><svg viewBox="0 0 12 12" aria-hidden="true"><path d="M0.5 2.5h11v7h-11z"/><path d="M0.5 2.5L6 7l5.5-4.5" fill="none" stroke="#f7f7f7" stroke-width="1"/></svg>jodiefarnsworth@brightnestly.com</li>
      </ul>
    </div>

    <svg class="footer-band" viewBox="0 0 480 40" aria-hidden="true">
      <rect x="0" y="23" width="240" height="10" fill="var(--brand-light)"/>
      <path d="M240 0H480V40H220Z" fill="var(--brand-deep)"/>
    </svg>
    <span class="website">www.BrightNestly.com</span>
  </section>
</main>
</body>
</html>
```